Flyer to advertise gutter cleaning throughout the Autumn and winter monthss

I need a new flyer to advertise gutter and driveway cleaning, roof and gutter repairs.

I am an experienced licensed Plumber and Gasfitter looking to broaden my scope of work to gutter cleaning. I am experienced in cleaning gutter and live in a area with large gum trees. I wont something that's clear, eye catching but not too busy.

Flyer requirements: Free roof inspection - no obligation. Gutter Cleaning from $199. Pictures of men using blower or hands to clean roof gutters (no obvious faces) to be included. Australian looking houses.

A mention that 'All general plumbing maintenance' is offered as other services but not too much wording about this as the target is for gutter cleaning.

Phone number: 0437 582 316 (in this format)
Business Name: Bracken Plumbing & Gasfitting
License: 3817502
ABN: 71395046287
Web: http://brackenplumbing.example-site.net/

Target Market(s)

Elderly - busy working class

Industry/Entity Type

Plumber

Font styles to use
Sans Serif

Colors
0355a3
fbed22
ec1f27
f78f20

Requirements
Must have
• Roof Gutter Cleaning pictures
• Men in protective clothing if possible
Nice to have
• More information:
• Prevent against flooding, mold, rust, rotting and corrosion now!
• Gutter Cleaning Services
• • Remove leaves, sticks, and other debris
• • Clear away clogs
• • Test your downpipes
• • Pinpoint any gutter issues
• • Repair gutter
• With regular service, you can count on your property to be well-protected no matter what the forecast!
Should not have
• Houses that don't look Australian

```html
<!DOCTYPE html>
<html lang="en">
<head>
<meta charset="utf-8">
<title>Bracken Plumbing &amp; Gasfitting – Gutter Cleaning Flyer</title>
<link rel="stylesheet" href="https://fonts.googleapis.com/css2?family=Oswald:wght@500;600&family=Questrial&family=Cinzel:wght@400&display=swap">
<style>
  :root {
    --backdrop: #e9e9e9;
    --paper: #ffffff;
    --brand-blue: #0e3d91;
    --brand-red: #e8204f;
    --ink: #2a2a2a;
    --roof-light: #e0774a;
    --roof-dark: #a9492a;
    --sky: #cfe2f3;
    --paving-light: #6a6e66;
    --paving-dark: #3a3d38;
  }
  * { margin: 0; padding: 0; box-sizing: border-box; }
  html, body { width: 1034px; height: 1200px; overflow: hidden; background: var(--backdrop); }
  .flyer {
    position: absolute; left: 93px; top: 0;
    width: 848px; height: 1200px;
    background: var(--paper); overflow: hidden;
  }
  .flyer-art { position: absolute; inset: 0; }
  .headline {
    position: absolute; left: 58px; color: #fff; white-space: nowrap;
    font-family: "Oswald", sans-serif; font-weight: 600;
    line-height: 1; letter-spacing: -0.5px;
    text-shadow: 0 2px 3px rgba(0,0,0,.55);
    transform-origin: left top;
  }
  .headline--service { font-size: 62px; }
  .headline--price { font-size: 94px; transform: scaleX(.82); }
  .headline--gutter { top: 73px; transform: scaleX(.78); }
  .headline--driveway { top: 231px; transform: scaleX(.68); }
  .headline--price-one { top: 126px; }
  .headline--price-two { top: 275px; }
  .offer-box {
    position: absolute; left: 56px; top: 421px;
    width: 312px; height: 173px;
    background: var(--brand-red); color: #fff;
    padding: 8px 0 0 30px; overflow: hidden;
  }
  .offer-box__line {
    display: block; white-space: nowrap;
    font-family: "Oswald", sans-serif; font-weight: 600;
    font-size: 58px; line-height: 1.0; letter-spacing: 1px;
    transform-origin: left top;
  }
  .offer-box__line--first { transform: scaleX(.94); }
  .offer-box__line--second { transform: scaleX(.85); }
  .offer-box__note {
    font-family: "Cinzel", serif; font-size: 27px; margin-top: 2px; letter-spacing: .5px; white-space: nowrap;
  }
  .benefits {
    position: absolute; left: 58px; top: 622px;
    font-family: "Questrial", sans-serif; font-size: 21.5px; color: var(--ink);
    list-style: none;
  }
  .benefits li { height: 31px; display: flex; align-items: center; white-space: nowrap; }
  .benefits .tick { width: 20px; height: 16px; margin-right: 10px; }
  .benefits .pair { margin-left: 8px; display: inline-flex; align-items: center; }
  .call-label {
    position: absolute; left: 64px; top: 755px; white-space: nowrap;
    font-family: "Oswald", sans-serif; font-weight: 500; font-size: 46px;
    color: var(--brand-blue); line-height: 1;
    transform: scaleX(.69); transform-origin: left top;
  }
  .call-number {
    position: absolute; left: 64px; top: 801px; white-space: nowrap;
    font-family: "Oswald", sans-serif; font-weight: 500; font-size: 72px;
    color: var(--brand-blue); line-height: 1;
    transform: scaleX(.72); transform-origin: left top;
  }
  .brand {
    position: absolute; left: 36px; top: 896px;
    display: flex; align-items: center; gap: 16px;
  }
  .brand__mark {
    width: 158px; height: 158px; border-radius: 50%; flex: none;
    background: #fff; border: 16px solid var(--brand-blue);
  }
  .brand__name {
    font-family: "Questrial", sans-serif; color: var(--ink); white-space: nowrap;
  }
  .brand__name-main { display: block; font-size: 29px; line-height: 1.05; }
  .brand__name-sub { display: block; font-size: 21px; line-height: 1.05; }
  .footer-web {
    position: absolute; left: 45px; top: 1096px; white-space: nowrap;
    font-family: "Questrial", sans-serif; font-size: 28px; color: #fff;
  }
  .footer-meta {
    position: absolute; top: 1150px; white-space: nowrap;
    font-family: "Questrial", sans-serif; font-size: 18px; color: #fff;
  }
  .footer-meta--licence { left: 46px; }
  .footer-meta--abn { left: 272px; }
  .social { position: absolute; left: 611px; top: 1145px; display: flex; gap: 6px; }
  .social span { width: 30px; height: 30px; border-radius: 50%; background: #fff; }
</style>
</head>
<body>
<main class="flyer">
  <svg class="flyer-art" width="848" height="1200" viewBox="0 0 848 1200">
    <defs>
      <linearGradient id="roofTone" x1="0" y1="0" x2="1" y2="1">
        <stop offset="0" stop-color="#e0774a"/>
        <stop offset="1" stop-color="#a9492a"/>
      </linearGradient>
      <linearGradient id="pavingTone" x1="0" y1="0" x2="1" y2="1">
        <stop offset="0" stop-color="#6a6e66"/>
        <stop offset="1" stop-color="#3a3d38"/>
      </linearGradient>
      <linearGradient id="workerTone" x1="0" y1="0" x2="0" y2="1">
        <stop offset="0" stop-color="#d9d6d1"/>
        <stop offset="1" stop-color="#f4f2ef"/>
      </linearGradient>
    </defs>

    <path d="M0 872 C150 990 350 1078 560 1074 C700 1070 800 1042 848 1020 V1200 H0 Z" fill="url(#pavingTone)" role="img" aria-label="Photo of a paved driveway beside a garden"/>
    <path class="band band--red" d="M0 868 C150 990 350 1078 560 1074 C700 1070 800 1042 848 1020 L848 1036 C800 1060 700 1090 560 1094 C340 1098 150 1010 0 896 Z" fill="#e8204f"/>

    <path class="band band--blue" d="M0 330 C40 380 120 420 200 436 C420 520 640 520 848 494 L848 506 C620 542 420 560 240 500 C140 470 60 430 0 380 Z" fill="#0e3d91"/>
    <path d="M0 0 H848 V492 C640 518 430 520 250 468 C150 440 60 400 0 338 Z" fill="url(#roofTone)" role="img" aria-label="Photo of a worker pressure-washing a terracotta tiled roof"/>
    <rect x="0" y="0" width="848" height="36" fill="#cfe2f3"/>

    <rect x="528" y="632" width="268" height="500" rx="40" fill="url(#workerTone)" role="img" aria-label="Photo of a man in work clothes using a pressure washer hose"/>
  </svg>

  <div class="headline headline--service headline--gutter">GUTTER CLEANING</div>
  <div class="headline headline--price headline--price-one">FROM $199</div>
  <div class="headline headline--service headline--driveway">DRIVEWAY CLEANING</div>
  <div class="headline headline--price headline--price-two">FROM $299</div>

  <section class="offer-box">
    <span class="offer-box__line offer-box__line--first">FREE ROOF</span>
    <span class="offer-box__line offer-box__line--second">INSPECTION</span>
    <div class="offer-box__note">NO OBLIGATION.</div>
  </section>

  <ul class="benefits">
    <li><svg class="tick" viewBox="0 0 20 16"><path d="M2 9 L7 14 L18 2" fill="none" stroke="#222" stroke-width="2.2"/></svg>Fully Insured<span class="pair"><svg class="tick" viewBox="0 0 20 16"><path d="M2 9 L7 14 L18 2" fill="none" stroke="#222" stroke-width="2.2"/></svg>Fast &amp; Safe</span></li>
    <li><svg class="tick" viewBox="0 0 20 16"><path d="M2 9 L7 14 L18 2" fill="none" stroke="#222" stroke-width="2.2"/></svg>Quality &amp; satisfaction<span class="pair"><svg class="tick" viewBox="0 0 20 16"><path d="M2 9 L7 14 L18 2" fill="none" stroke="#222" stroke-width="2.2"/></svg>Free inspection</span></li>
    <li><svg class="tick" viewBox="0 0 20 16"><path d="M2 9 L7 14 L18 2" fill="none" stroke="#222" stroke-width="2.2"/></svg>Professional &amp; affordable</li>
    <li><svg class="tick" viewBox="0 0 20 16"><path d="M2 9 L7 14 L18 2" fill="none" stroke="#222" stroke-width="2.2"/></svg>Kid &amp; pet friendly</li>
  </ul>

  <div class="call-label">CALL US FOR A FREE</div>
  <div class="call-number">0437 582 316</div>

  <div class="brand">
    <div class="brand__mark"></div>
    <div class="brand__name">
      <span class="brand__name-main">BRACKEN PLUMBING</span>
      <span class="brand__name-sub">&amp; GASFITTING</span>
    </div>
  </div>

  <div class="footer-web">BrackenPlumbing.example-site.net</div>
  <div class="footer-meta footer-meta--licence">License: 3817502</div>
  <div class="footer-meta footer-meta--abn">ABN: 71395046287</div>
  <div class="social"><span></span><span></span><span></span><span></span><span></span></div>
</main>
</body>
</html>
```